Internet Flyer for Voip and Fast Internet

I need a 2 sided A5 flyer for a bespoke service to residential flats...

Needs to stand out after dropping through the door...!

Target Market(s)

Central City Flats - High value occupants.

Industry/Entity Type

Residential

```html
<!DOCTYPE html>
<html lang="en">
<head>
<meta charset="utf-8">
<title>Northvane Telecom – Four Play Flyer</title>
<link rel="stylesheet" href="https://fonts.googleapis.com/css2?family=Arimo:wght@400;700&family=Roboto+Condensed:wght@400;700&display=swap">
<style>
  :root {
    --stage: #3b3b3b;
    --ink: #050705;
    --white: #f2f4f2;
    --green: #4cc43a;
    --grey: #8a8f8a;
    --label: #f4f4f4;
  }
  * { box-sizing: border-box; margin: 0; padding: 0; }
  html, body { width: 1200px; height: 927px; overflow: hidden; }
  body {
    background: radial-gradient(ellipse at 50% 40%, #5a5a5a 0%, #2e2e2e 80%);
    font-family: "Roboto Condensed", "Arial Narrow", sans-serif;
    color: var(--white);
    position: relative;
  }
  .side-label {
    position: absolute; top: 66px;
    font-family: "Arimo", Arial, sans-serif; font-size: 24px; color: var(--label);
  }
  .side-label--front { left: 91px; }
  .side-label--back { left: 633px; }
  .flyer {
    position: absolute;
    top: 118px;
    width: 474px;
    height: 672px;
    background: var(--ink);
    overflow: hidden;
    box-shadow: 0 10px 30px rgba(0,0,0,.5);
  }
  .flyer--front { left: 91px; }
  .flyer--back { left: 633px; }
  .flyer__art { position: absolute; top: 0; left: 0; width: 474px; height: 672px; }
  .flyer__graphic {
    position: absolute; top: 0; right: 0; width: 280px; height: 280px;
    background: radial-gradient(circle at 60% 35%, #9a9e9a 0%, #4a4e4a 35%, rgba(10,12,10,0) 72%);
    opacity: .75;
  }
  .flyer__content {
    position: absolute; top: 52px; left: 28px; width: 360px;
    transform: rotate(5deg); transform-origin: top left;
  }
  .headline {
    font-family: "Arimo", Arial, sans-serif;
    font-size: 29px; line-height: 1.05; font-weight: 400;
  }
  .headline__accent { color: var(--green); font-weight: 700; display: block; }
  .tagline { font-family: "Arimo", Arial, sans-serif; font-size: 19px; margin-top: 2px; }
  .rule { border-top: 2px dashed var(--grey); margin: 8px 0 7px; }
  .intro { font-size: 12px; text-align: right; text-transform: uppercase; line-height: 1.2; }
  .intro em { font-style: normal; color: var(--green); }
  .offer-title { font-size: 23px; margin: 6px 0 4px; text-transform: uppercase; font-weight: 400; }
  .package { text-align: right; text-transform: uppercase; font-size: 11px; line-height: 1.15; margin-bottom: 6px; }
  .package__title { color: var(--green); font-size: 13px; }
  .note { text-align: right; text-transform: uppercase; font-size: 10.5px; line-height: 1.18; margin-top: 10px; }
  .company {
    position: absolute; right: 34px; bottom: 20px;
    font-family: "Arimo", Arial, sans-serif; font-size: 16px;
  }
  .web {
    position: absolute; bottom: 24px;
    font-size: 9px; letter-spacing: 2px; color: var(--white);
    writing-mode: vertical-rl; transform: rotate(180deg);
    white-space: nowrap;
  }
  .flyer--front .web { right: 12px; }
  .flyer--back .web { left: 12px; bottom: 40px; }
  .benefits { margin-top: 4px; }
  .benefit { text-transform: uppercase; font-size: 9.5px; line-height: 1.08; text-align: right; margin-bottom: 6px; }
</style>
</head>
<body>

<p class="side-label side-label--front">Front</p>
<p class="side-label side-label--back">Back</p>

<section class="flyer flyer--front">
  <svg class="flyer__art" viewBox="0 0 560 792" preserveAspectRatio="none" aria-hidden="true">
    <defs>
      <linearGradient id="band" x1="1" y1="0" x2="0" y2="1">
        <stop offset="0" stop-color="#2a8f28"/>
        <stop offset=".5" stop-color="#145c16"/>
        <stop offset="1" stop-color="#0a2a0b"/>
      </linearGradient>
    </defs>
    <polygon points="560,120 560,330 0,792 0,600" fill="url(#band)" opacity=".85"/>
    <polygon points="560,330 560,420 120,792 0,792" fill="#0b300c" opacity=".7"/>
  </svg>
  <div class="flyer__graphic" role="img" aria-label="Abstract grey circuit lines and ring graphic"></div>
  <div class="flyer__content">
    <h1 class="headline">Making an <span class="headline__accent">EVEN BETTER</span> investment!</h1>
    <div class="rule"></div>
    <p class="intro">Are you fed up with <em>slow internet</em><br>and <em>expensive</em> phone calls?</p>
    <div class="rule"></div>
    <h2 class="offer-title">Try our “Four Play”</h2>
    <div class="package">
      <p class="package__title">Phone packages</p>
      <p>Available now<br>Line rental only £4.99 per month<br>Cheap calls to the world<br>Eg USA – 1p per min, China 2p per min<br>Free calls to the same network</p>
    </div>
    <div class="package">
      <p class="package__title">Internet packages</p>
      <p>Sign up now<br>100Mbs up and down<br>£249 install and £99.00 per month<br>Faster speeds are available – up to 1 Gbs</p>
    </div>
    <div class="package">
      <p class="package__title">TV and HiFi over the internet</p>
      <p>Tell us what services you need<br>Soundhall – Tunebox, Melodix etc<br>Lumatek<br>IPTV<br>Etc etc</p>
    </div>
    <div class="package">
      <p class="package__title">Corvia Telepresence</p>
      <p>Contact us for further information!</p>
    </div>
    <p class="note">Remember! The TV program 24?<br>Do you need to connect with people?<br>We are able to connect you to<br>the video world to give you high definition 50”<br>+ video calls and conferencing</p>
  </div>
  <p class="company">Northvane Telecom Group Ltd</p>
  <p class="web">http://www.northvane-networks.net</p>
</section>

<section class="flyer flyer--back">
  <svg class="flyer__art" viewBox="0 0 560 792" preserveAspectRatio="none" aria-hidden="true">
    <defs>
      <linearGradient id="bandBack" x1="1" y1="0" x2="0" y2="1">
        <stop offset="0" stop-color="#2a8f28"/>
        <stop offset=".55" stop-color="#145c16"/>
        <stop offset="1" stop-color="#0a2a0b"/>
      </linearGradient>
    </defs>
    <polygon points="560,60 560,470 60,792 0,792 0,380" fill="url(#bandBack)" opacity=".85"/>
  </svg>
  <div class="flyer__graphic" role="img" aria-label="Abstract grey circuit lines and ring graphic"></div>
  <div class="flyer__content">
    <h1 class="headline">Making an <span class="headline__accent">EVEN BETTER</span> investment!</h1>
    <p class="tagline">TRY OUR “FOUR PLAY”</p>
    <div class="rule"></div>
    <div class="benefits">
      <p class="benefit">Delay kills all forms of human interaction<br>and creativity. Less delay results in more<br>effective interaction, innovation and output<br>and the relationship is highly non-linear so<br>less delay translates into far more output</p>
      <p class="benefit">Ubiquitous (and symmetrical) videoconferencing<br>that actually works can dramatically<br>reduce our need to travel</p>
      <p class="benefit">Real-time multi-user collaborative environments<br>can further accelerate (global)<br>creativity and productivity<br>by making virtual teaming a working reality</p>
      <p class="benefit">Imagine instantaneous access to information<br>sources and resources of all kinds of<br>forms and formats – uploads and downloads</p>
      <p class="benefit">Cloud computing with all applications and<br>data online would dramatically reduce<br>hardware and software costs, improve security<br>markedly and spawn new communities, business<br>opportunities and industries</p>
      <p class="benefit">Virtual and augmented reality would come<br>alive and change absolutely everything from<br>working to entertainment, education, training<br>and healthcare – and we can't even hazard a<br>guess at the scale of improvement to be had</p>
      <p class="benefit">All forms of modelling and prediction<br>scientific, industrial, social and so on would be<br>transformed by instant access to distributed<br>resources worldwide</p>
      <p class="benefit">3D prototyping and distributed production<br>would become real and a part of the mainstream,<br>and ultimately the new mainstream industry</p>
      <p class="benefit">Real-time access to global radio, TV, movies<br>and other forms of entertainment<br>at our convenience</p>
      <p class="benefit">Vast tracts of radio spectrum for<br>high-speed wireless apps would become<br>available as services delivered by ‘by fibre’<br>reduce the need for services ‘by radio’</p>
    </div>
  </div>
  <p class="web">http://www.northvane-networks.net</p>
</section>

</body>
</html>
```